Flyer Design Project

Advertising - The header is the most important thing on this flyer, I would like to see an eyes-popping more in dept look of the clouds along with the sport car of the couple on the road. The symbol of the "Lantern Over Amber Hills" don't want it there. Just replace it with a regular "i".

Industry/Entity Type

Advertising

Requirements
Must have
• head turning... stopping prospects to read the flyer... everything got to be on point from art works to different fonts and style.

```html
<!DOCTYPE html>
<html lang="en">
<head>
<meta charset="utf-8">
<title>Lantern Over Amber Hills – Flyer</title>
<link href="https://fonts.googleapis.com/css2?family=Montserrat:ital,wght@1,800;1,900&family=Fira+Sans:ital,wght@0,300;0,400;0,700;1,300;1,400;1,700&family=Roboto+Condensed:wght@700&display=swap" rel="stylesheet">
<style>
  :root {
    --sky-top: #cfe3f5;
    --sky-mid: #e9f2fa;
    --paper: #ffffff;
    --ink: #1c1c1c;
    --body: #2b2b2b;
    --blue: #1f7fd4;
    --blue-deep: #1266b8;
    --red: #e0141b;
    --badge: #efb85c;
    --badge-edge: #e8804a;
    --column-top: #55a4ec;
    --column-bottom: #3a78b8;
    --navy: #1b2a4e;
  }
  * { box-sizing: border-box; margin: 0; padding: 0; }
  html, body { width: 960px; height: 1200px; overflow: hidden; background: var(--paper); }
  .flyer {
    position: relative; width: 960px; height: 1200px; overflow: hidden;
    font-family: "Fira Sans", Arial, sans-serif; color: var(--body);
    background: linear-gradient(180deg, var(--sky-top) 0%, var(--sky-mid) 30%, #f7fafd 48%, var(--paper) 60%);
  }
  .sky-scene {
    position: absolute; inset: 0 0 auto 0; height: 470px;
    background:
      radial-gradient(ellipse 220px 90px at 820px 40px, rgba(255,255,255,.9), transparent 70%),
      radial-gradient(ellipse 260px 80px at 500px 330px, rgba(255,255,255,.85), transparent 70%),
      radial-gradient(ellipse 200px 70px at 900px 250px, rgba(255,255,255,.8), transparent 70%),
      linear-gradient(180deg, #a9cdee 0%, #d8e8f6 55%, rgba(255,255,255,0) 100%);
  }
  .road-scene {
    position: absolute; left: 0; top: 0; width: 380px; height: 300px;
    background:
      radial-gradient(ellipse 150px 110px at 150px 150px, rgba(255,140,40,.95), rgba(255,120,40,.4) 60%, transparent 80%),
      radial-gradient(ellipse 160px 120px at 120px 240px, rgba(90,130,190,.8), transparent 75%),
      linear-gradient(160deg, #c6602a 0%, #e89a4c 30%, rgba(200,210,230,.4) 70%, rgba(255,255,255,0) 100%);
    -webkit-mask-image: radial-gradient(ellipse 340px 280px at 0 0, #000 55%, transparent 100%);
            mask-image: radial-gradient(ellipse 340px 280px at 0 0, #000 55%, transparent 100%);
  }
  .headline { font-family: "Montserrat", sans-serif; font-style: italic; font-weight: 900; }
  .headline span { position: absolute; display: block; line-height: 1; white-space: nowrap; }
  .headline .kicker { left: 352px; top: 52px; font-size: 44px; color: #0d0d0d; letter-spacing: -1px; }
  .headline .main { right: 58px; top: 100px; font-size: 100px; color: var(--blue); letter-spacing: -3px;
    text-shadow: 3px 3px 0 rgba(0,40,90,.18); }
  .headline .accent { right: 118px; top: 184px; font-size: 54px; color: var(--red); letter-spacing: -1px; }
  .tagline { position: absolute; left: 362px; top: 246px; font-style: italic; font-weight: 300; font-size: 23px; line-height: 1.1; color: #1a1a1a; white-space: nowrap; }

  .intro { position: absolute; left: 48px; top: 308px; width: 540px; }
  .section-title { font-weight: 700; font-size: 27px; line-height: 1.02; color: var(--ink); }
  .body-copy { font-weight: 300; font-size: 17px; line-height: 21.6px; color: var(--body); margin-top: 14px; }
  .body-copy strong { font-weight: 700; color: #111; }
  .body-copy + .body-copy { margin-top: 21px; }

  .how-title { position: absolute; left: 48px; top: 528px; font-weight: 700; font-size: 27px; color: var(--ink); }
  .steps { position: absolute; left: 54px; top: 574px; width: 460px; list-style: none; }
  .step { position: relative; padding-left: 48px; font-weight: 300; font-size: 17px; line-height: 21.6px; min-height: 36px; margin-bottom: 6px; padding-top: 6px; }
  .step-num { position: absolute; left: 0; top: 0; width: 35px; height: 35px; border-radius: 50%; background: var(--blue-deep); color: #fff;
    font-weight: 700; font-size: 19px; display: flex; align-items: center; justify-content: center; }

  .never-title { position: absolute; left: 48px; top: 732px; font-weight: 700; font-size: 29px; color: var(--ink); letter-spacing: -.2px; }
  .perks { position: absolute; left: 52px; top: 774px; width: 520px; list-style: none; }
  .perk { position: relative; padding-left: 24px; font-weight: 300; font-size: 17px; line-height: 21.6px; margin-bottom: 8.4px; }
  .perk svg { position: absolute; left: 0; top: 1px; width: 18px; height: 20px; }
  .perk b { color: var(--red); font-weight: 700; }

  .info-column { position: absolute; left: 621px; top: 440px; width: 294px; height: 650px;
    background: linear-gradient(180deg, var(--column-top) 0%, #4a90d4 50%, var(--column-bottom) 100%); }
  .badge { position: absolute; left: 620px; top: 310px; width: 296px; height: 296px; border-radius: 50%; background: var(--badge);
    box-shadow: 0 8px 0 var(--badge-edge); text-align: center; padding-top: 46px; }
  .badge p { font-weight: 700; font-style: italic; font-size: 24px; line-height: 30.5px; color: #3b2a12; }
  .badge .cta { font-style: normal; font-size: 29px; line-height: 34px; color: #0d0d0d; margin-top: 12px; }

  .contact { position: absolute; left: 621px; top: 656px; width: 294px; text-align: center; color: #fff; font-weight: 300; }
  .hours { font-size: 18px; line-height: 24.8px; }
  .phone { font-weight: 700; font-size: 31px; margin-top: 16px; letter-spacing: .3px; }
  .pin-note { font-size: 17.5px; line-height: 23px; margin-top: 18px; }
  .pin-note strong { font-weight: 700; }
  .line-label { font-size: 17.5px; margin-top: 22px; }
  .line-phone { font-weight: 700; font-size: 23px; line-height: 1; }
  .line-hint { font-style: italic; font-size: 12px; margin-top: 8px; }
  .site { font-size: 18px; margin-top: 28px; }

  .footer-band { position: absolute; left: 0; top: 1090px; width: 960px; height: 110px; background: var(--navy); color: #fff; }
  .footer-band p { font-family: "Roboto Condensed", sans-serif; font-weight: 700; font-size: 18px; line-height: 21.6px; text-align: center; padding: 22px 50px 0; text-transform: uppercase; }
  .footer-band small { position: absolute; right: 60px; bottom: 12px; font-style: italic; font-weight: 300; font-size: 11.5px; }
</style>
</head>
<body>
<main class="flyer">
  <div class="sky-scene" role="img" aria-label="Bright blue sky with soft white clouds"></div>
  <div class="road-scene" role="img" aria-label="Couple driving a sports car along a sunlit road"></div>

  <h1 class="headline">
    <span class="kicker">LANTERN OVER</span>
    <span class="main">AMBER</span>
    <span class="accent">HILLS</span>
  </h1>
  <p class="tagline">The best way to predict your future is to create it.</p>

  <section class="intro">
    <h2 class="section-title">What’s the #1 Success Factor<br>in Every Home-Based Business?</h2>
    <p class="body-copy">The answer is <strong>DUPLICATION!</strong> The key to building a highly successful homebased business is having a <strong>SYSTEM</strong> in place that everyone can easily follow... <strong>WE HAVE THAT SYSTEM IN PLACE!</strong></p>
    <p class="body-copy">It’s a simple 3 steps proven postcard system that you can plug in immediately. <em style="font-weight:400">The Entire Process Is Automated.</em></p>
  </section>

  <h2 class="how-title">HERE’S HOW IT WORKS!</h2>
  <ol class="steps">
    <li class="step"><span class="step-num">1</span>Your prospects receive your postcard in the mail.</li>
    <li class="step"><span class="step-num">2</span>They listen to the 24-Hour Information Line and</li>
    <li class="step"><span class="step-num">3</span>They contact the Call Center to get their questions<br>answer and then close the sales for you.</li>
  </ol>

  <h2 class="never-title">YOU NEVER HAVE TO SPEAK TO ANYONE!</h2>
  <ul class="perks">
    <li class="perk"><svg viewBox="0 0 18 20"><path d="M1 11 L6 18 L17 1 L6 13 Z" fill="#111"/></svg>50% fast start bonuses <b>PAID WEEKLY!</b></li>
    <li class="perk"><svg viewBox="0 0 18 20"><path d="M1 11 L6 18 L17 1 L6 13 Z" fill="#111"/></svg>Receive a 100% Matching Bonus on all your personal sponsor member’s income <b>PAID WEEKLY!</b></li>
    <li class="perk"><svg viewBox="0 0 18 20"><path d="M1 11 L6 18 L17 1 L6 13 Z" fill="#111"/></svg>One-of-a-kind <b>TWO TEAM</b> compensation plan!</li>
    <li class="perk"><svg viewBox="0 0 18 20"><path d="M1 11 L6 18 L17 1 L6 13 Z" fill="#111"/></svg>Receive the choice of <b>50 FREE POST CARDS</b> and <b>50 FREE<br>LEADS</b> or 20 home business surveyed leads with first month product purchase!</li>
    <li class="perk"><svg viewBox="0 0 18 20"><path d="M1 11 L6 18 L17 1 L6 13 Z" fill="#111"/></svg>Receive <b>THREE</b> professional websites for your business for <b>FREE!</b></li>
    <li class="perk"><svg viewBox="0 0 18 20"><path d="M1 11 L6 18 L17 1 L6 13 Z" fill="#111"/></svg>Global business already shipping to over 45 countries worldwide and expanding.</li>
    <li class="perk"><svg viewBox="0 0 18 20"><path d="M1 11 L6 18 L17 1 L6 13 Z" fill="#111"/></svg>30-Day - No Questions Asked, 100% Money Back Guarantee!</li>
  </ul>

  <aside class="info-column"></aside>
  <div class="badge">
    <p>100’s of people<br>are joining every day<br>and taking advantage<br>of this once-in-alifetime<br>opportunity.</p>
    <p class="cta">DON’T MISS<br>OUT!</p>
  </div>

  <div class="contact">
    <p class="hours">CALL CENTER HOURS<br>Monday thru Friday<br>12PM to 9PM EST<br>Saturday: 12PM to 5PM EST</p>
    <p class="phone">(555) 014-2273</p>
    <p class="pin-note">You will need the Call Center<br>Pin number when calling!<br><strong>Call Center Pin<br>Number: M2519</strong></p>
    <p class="line-label">24-Hour Information Line:</p>
    <p class="line-phone">(555) 019-3346</p>
    <p class="line-hint">(Listen before contacting the Call Center)</p>
    <p class="site">www.amberhillsroute.com</p>
  </div>

  <footer class="footer-band">
    <p>Due to the high volume of callers, if lines are busy, please keep trying to call into the call center or you can just go to the website and get enrolled right away to secure a top position.</p>
    <small>© 2016 Hillside Beacon Marketing Group</small>
  </footer>
</main>
</body>
</html>
```